Website Header for new website

We need a header/banner design for our revised website. Here is the link to our existing website lorimakwell.me and to our new website in process agewiseplus.us
Area of expertise is older adults, baby boomers and caregivers
This is an individual, professional website for a Speaker, Keynoter, Author, Brocaster

Target Market(s)

Event planners, broadcasters, publishers

Font styles to use
Serif

```html
<!DOCTYPE html>
<html lang="en">
<head>
<meta charset="UTF-8">
<title>Lori Makwell — Speaker Header</title>
<link rel="stylesheet" href="https://fonts.googleapis.com/css2?family=Playfair+Display:ital@1&family=Questrial&display=swap">
<style>
  :root {
    --audience-dark: #2a2622;
    --audience-mid: #4a423b;
    --audience-warm: #6b5a4c;
    --stage-wall: #8a7b6d;
    --portrait-orange: #d4581f;
    --portrait-skin: #d9b79c;
    --portrait-hair: #d8c49a;
    --text-light: #ffffff;
  }
  * { margin: 0; padding: 0; box-sizing: border-box; }
  html, body { width: 1200px; height: 402px; overflow: hidden; background: var(--audience-dark); }
  .header-banner { position: relative; width: 1200px; height: 402px; overflow: hidden; }
  .audience-backdrop {
    position: absolute; inset: 0;
    background:
      linear-gradient(180deg, rgba(138,123,109,0.55) 0%, rgba(0,0,0,0) 30%),
      radial-gradient(ellipse at 70% 60%, var(--audience-warm) 0%, var(--audience-mid) 45%, var(--audience-dark) 100%);
  }
  .audience-shade { position: absolute; inset: 0; background: linear-gradient(90deg, rgba(0,0,0,0.15) 0%, rgba(0,0,0,0.45) 55%, rgba(0,0,0,0.2) 100%); }
  .speaker-portrait {
    position: absolute; left: 116px; top: 12px; width: 240px; height: 390px;
    border-radius: 90px 90px 12px 12px;
    background: linear-gradient(180deg, var(--portrait-hair) 0%, var(--portrait-skin) 22%, var(--portrait-orange) 36%, #c54f1c 70%, #5a4a44 100%);
  }
  .speaker-name {
    position: absolute; left: 398px; top: 104px;
    font-family: "Playfair Display", Georgia, serif; font-style: italic; font-weight: 400;
    font-size: 35px; color: var(--text-light); letter-spacing: 0.3px;
  }
  .role-list {
    position: absolute; left: 400px; top: 176px; list-style: none;
    display: grid; grid-template-columns: 228px 220px; row-gap: 13px;
    font-family: "Questrial", Arial, sans-serif; font-size: 15.5px; color: var(--text-light);
  }
  .role-item { display: flex; align-items: center; gap: 12px; height: 23px; }
  .tick-icon { width: 18px; height: 18px; flex: none; }
</style>
</head>
<body>
<header class="header-banner">
  <div class="audience-backdrop" role="img" aria-label="Blurred photo of a large seated conference audience in a lecture hall"></div>
  <div class="audience-shade"></div>
  <div class="speaker-portrait" role="img" aria-label="Portrait photo of the speaker in an orange jacket and ruffled blouse"></div>
  <h1 class="speaker-name">Lori Makwell</h1>
  <ul class="role-list">
    <li class="role-item"><svg class="tick-icon" viewBox="0 0 18 18"><path d="M15.2 7.6A6.6 6.6 0 1 1 11.8 3" fill="none" stroke="#fff" stroke-width="1.8" stroke-linecap="round"/><path d="M5.6 8.4l3 3 7.2-7.4" fill="none" stroke="#fff" stroke-width="2" stroke-linecap="round" stroke-linejoin="round"/></svg>Dynamic Keynote</li>
    <li class="role-item"><svg class="tick-icon" viewBox="0 0 18 18"><path d="M15.2 7.6A6.6 6.6 0 1 1 11.8 3" fill="none" stroke="#fff" stroke-width="1.8" stroke-linecap="round"/><path d="M5.6 8.4l3 3 7.2-7.4" fill="none" stroke="#fff" stroke-width="2" stroke-linecap="round" stroke-linejoin="round"/></svg>Prolific Auther</li>
    <li class="role-item"><svg class="tick-icon" viewBox="0 0 18 18"><path d="M15.2 7.6A6.6 6.6 0 1 1 11.8 3" fill="none" stroke="#fff" stroke-width="1.8" stroke-linecap="round"/><path d="M5.6 8.4l3 3 7.2-7.4" fill="none" stroke="#fff" stroke-width="2" stroke-linecap="round" stroke-linejoin="round"/></svg>Motivation Speaker</li>
    <li class="role-item"><svg class="tick-icon" viewBox="0 0 18 18"><path d="M15.2 7.6A6.6 6.6 0 1 1 11.8 3" fill="none" stroke="#fff" stroke-width="1.8" stroke-linecap="round"/><path d="M5.6 8.4l3 3 7.2-7.4" fill="none" stroke="#fff" stroke-width="2" stroke-linecap="round" stroke-linejoin="round"/></svg>Enterainting Blogger</li>
    <li class="role-item"><svg class="tick-icon" viewBox="0 0 18 18"><path d="M15.2 7.6A6.6 6.6 0 1 1 11.8 3" fill="none" stroke="#fff" stroke-width="1.8" stroke-linecap="round"/><path d="M5.6 8.4l3 3 7.2-7.4" fill="none" stroke="#fff" stroke-width="2" stroke-linecap="round" stroke-linejoin="round"/></svg>Influential Broadcaster</li>
    <li class="role-item"><svg class="tick-icon" viewBox="0 0 18 18"><path d="M15.2 7.6A6.6 6.6 0 1 1 11.8 3" fill="none" stroke="#fff" stroke-width="1.8" stroke-linecap="round"/><path d="M5.6 8.4l3 3 7.2-7.4" fill="none" stroke="#fff" stroke-width="2" stroke-linecap="round" stroke-linejoin="round"/></svg>Effective Trainer</li>
  </ul>
</header>
</body>
</html>
```